Business Card Designs

Looking to design a 3.5" x 2" standard business card for our employees.
The design needs to be sleek, simple, and modern. We would like our logo (attached) to be incorporated, but not in that colour, rather an outline of the logo in either gold or silver (whichever looks better).

Modern and Simple is what we are looking for, but be creative in incorporating the logo.

```html
<!DOCTYPE html>
<html lang="en">
<head>
<meta charset="utf-8">
<title>Lakeview Loft Apartments – Business Card</title>
<link href="https://fonts.googleapis.com/css2?family=Roboto+Condensed:wght@400;700&family=Roboto:wght@400&display=swap" rel="stylesheet">
<style>
  :root {
    --backdrop: #b8b8b8;
    --card: #000000;
    --gold: #ffc21a;
    --gold-deep: #ffa000;
    --text-light: #d0d0d0;
    --rule: #6a6a6a;
  }
  html, body {
    margin: 0;
    padding: 0;
    width: 1200px;
    height: 1200px;
    overflow: hidden;
    background: var(--backdrop);
  }
  .canvas {
    position: relative;
    width: 1200px;
    height: 1200px;
  }
  .card {
    position: absolute;
    top: 303px;
    width: 368px;
    height: 594px;
    background: var(--card);
    text-align: center;
    font-family: "Roboto", sans-serif;
  }
  .card--front { left: 200px; }
  .card--back { left: 599px; width: 364px; }

  .brand-mark {
    position: absolute;
    left: 50%;
    transform: translateX(-50%);
    background: var(--gold);
  }
  .card--front .brand-mark { top: 150px; width: 72px; height: 72px; }
  .card--back .brand-mark { top: 78px; width: 56px; height: 56px; }

  .brand-name {
    position: absolute;
    left: 0;
    right: 0;
    margin: 0;
    font-family: "Roboto Condensed", sans-serif;
    font-weight: 700;
    color: var(--gold);
    text-transform: uppercase;
    line-height: 1.25;
  }
  .card--front .brand-name {
    top: 400px;
    font-size: 26px;
    letter-spacing: 4px;
  }
  .card--back .brand-name {
    top: 258px;
    font-size: 18px;
    letter-spacing: 3px;
  }

  .person {
    position: absolute;
    top: 346px;
    left: 0;
    right: 0;
  }
  .person__name {
    margin: 0;
    font-family: "Roboto Condensed", sans-serif;
    font-weight: 700;
    font-size: 26px;
    letter-spacing: 1px;
    color: var(--gold);
    line-height: 1.1;
  }
  .person__role {
    margin: 0;
    font-size: 16px;
    color: var(--text-light);
    letter-spacing: 0.3px;
    line-height: 1.1;
  }

  .icon-row {
    position: absolute;
    top: 403px;
    left: 0;
    right: 0;
    display: flex;
    justify-content: center;
    align-items: center;
    gap: 4px;
  }
  .icon-row__rule {
    width: 52px;
    height: 1px;
    background: var(--rule);
    margin: 0 3px;
  }
  .icon-tile {
    width: 25px;
    height: 25px;
    border-radius: 4px;
    background: linear-gradient(var(--gold), var(--gold-deep));
    display: flex;
    align-items: center;
    justify-content: center;
  }
  .icon-tile svg { width: 16px; height: 16px; }

  .contact {
    position: absolute;
    top: 434px;
    left: 0;
    right: 0;
    margin: 0;
    font-size: 16px;
    line-height: 21px;
    color: var(--text-light);
    font-style: normal;
  }
  .divider {
    position: absolute;
    top: 509px;
    left: 88px;
    right: 82px;
    height: 1px;
    background: var(--rule);
  }
  .address {
    position: absolute;
    top: 520px;
    left: 0;
    right: 0;
    margin: 0;
    font-size: 16px;
    line-height: 21px;
    color: var(--text-light);
    font-style: normal;
  }
</style>
</head>
<body>
<main class="canvas">

  <section class="card card--front" aria-label="Card front">
    <div class="brand-mark"></div>
    <h1 class="brand-name">Lakeview Loft<br>Apartments</h1>
  </section>

  <section class="card card--back" aria-label="Card back">
    <div class="brand-mark"></div>
    <h2 class="brand-name">Lakeview Loft<br>Apartments</h2>

    <div class="person">
      <p class="person__name">DANIEL MOORE</p>
      <p class="person__role">MANAGING DIRECTOR</p>
    </div>

    <div class="icon-row">
      <span class="icon-row__rule"></span>
      <span class="icon-tile" aria-label="Phone">
        <svg viewBox="0 0 16 16"><path d="M2 6c0-2 3-3 6-3s6 1 6 3v1h-3V5.5H5V7H2z M4 8h8l1 5H3z" fill="#111"/></svg>
      </span>
      <span class="icon-tile" aria-label="Email">
        <svg viewBox="0 0 16 16"><rect x="2" y="4" width="12" height="8" fill="none" stroke="#111" stroke-width="1.2"/><path d="M2 4l6 5 6-5M2 12l4.5-4M14 12l-4.5-4" fill="none" stroke="#111" stroke-width="1"/></svg>
      </span>
      <span class="icon-tile" aria-label="Website">
        <svg viewBox="0 0 16 16"><circle cx="8" cy="8" r="6" fill="#111"/><path d="M5 5c1 0 2 1 1.5 2S5 8 6 10M10 4c0 1.5 1.5 2 2 3M9 10c1 0 2 1 1.5 2.5" fill="none" stroke="var(--gold)" stroke-width="1.2"/></svg>
      </span>
      <span class="icon-row__rule"></span>
    </div>

    <address class="contact">
      044-555 010 234<br>
      hello@lakeviewloft.com<br>
      www.lakeviewloft.com
    </address>

    <div class="divider"></div>

    <address class="address">
      421, Address line goes here<br>
      45452,Country Name
    </address>
  </section>

</main>
</body>
</html>
```